Online Greeting Card Marketplace redesign

QuillPostly.com is a two-sided greeting card marketplace. Buyers purchase hand-made cards online, indicating their message. Sellers hand-write the message and mail directly to recipient.

We are getting decent foot traffic but low sales. I'm also not drawing a lot of Card Designers to sell their products. Feedback has been that it's cluttered, boring, and out of date.

I've always enjoyed vibes such as Dana Whitlock and Rosalind Perry. I was going for pale blues and chocolate browns (as can be seen in QuillPostly Facebook and Twitter pages).

Attached document is my not-so-great attempt to redesign, which is uninviting and unpolished.

Need a new homepage and a second similar page when shopping (click on any category to see what I mean, e.g. Halloween).

Industry/Entity Type

Shopping

Requirements
Must have
• I think my logo (stick drawing of a man with an envelope) is what is currently driving a lot of traffic and should stay in the design, pending minor tweaks.

I'll need all the details of the final design to give to the programmers (font styles, color numbers, etc).

Nice to have
• I was thinking of a dotted frame to surround each picture? Frost Glimmer luminescent or a metallic? I just don't know if it works.

```html
<!DOCTYPE html>
<html lang="en">
<head>
<meta charset="utf-8">
<title>QuillPostly.com – Hand-made cards</title>
<link rel="stylesheet" href="https://fonts.googleapis.com/css2?family=PT+Sans:wght@400;700&family=PT+Sans+Narrow:wght@400;700&display=swap">
<style>
  :root {
    --ink-dark: #3a3a3a;
    --top-rule: #3c3c3c;
    --link-blue: #2f6fb5;
    --title-blue: #2a7cc2;
    --nav-grey: #8c9496;
    --band-grey: #efefef;
    --step-blue: #4b7fc4;
    --step-mid: #a3abad;
    --step-dark: #7d898b;
    --frame-dot: #c9c9c9;
    --footer-black: #0d0d0d;
    --white: #ffffff;
    --muted: #5a5a5a;
  }
  * { box-sizing: border-box; margin: 0; padding: 0; }
  html, body { width: 939px; height: 1200px; overflow: hidden; background: var(--white); }
  body { position: relative; font-family: "PT Sans", Arial, sans-serif; color: var(--ink-dark); }
  .abs { position: absolute; }

  .top-rule { left: 0; top: 0; width: 939px; height: 4px; background: var(--top-rule); }

  .utility-nav { left: 0; top: 19px; width: 939px; display: flex; justify-content: center; font-family: "PT Sans Narrow", sans-serif; font-size: 12.5px; }
  .utility-nav a { color: var(--link-blue); text-decoration: none; padding: 0 14px; border-left: 1px dotted #bbb; line-height: 16px; }
  .utility-nav a:first-child { border-left: none; }

  .brand { left: 300px; top: 84px; display: flex; align-items: center; gap: 12px; }
  .brand-mark { width: 26px; height: 26px; background: var(--step-blue); }
  .brand-name { font-size: 29px; color: var(--ink-dark); font-weight: 400; }
  .brand-tagline { left: 378px; top: 120px; font-size: 12px; color: var(--muted); }

  .cart { left: 770px; top: 103px; font-size: 12.5px; color: var(--ink-dark); display: flex; align-items: center; gap: 6px; }

  .category-bar { left: 68px; top: 169px; width: 803px; height: 42px; background: var(--nav-grey); }
  .category-list { list-style: none; font-family: "PT Sans Narrow", sans-serif; font-size: 15.5px; color: var(--white); }
  .category-list li { position: absolute; top: 12px; white-space: nowrap; }
  .search { left: 617px; top: 8px; width: 177px; height: 26px; background: var(--white); border: 1px solid #d8d8d8; border-radius: 2px; font-size: 10px; font-style: italic; color: #999; padding: 7px 9px; }
  .search svg { position: absolute; right: 8px; top: 7px; }

  .steps-band { left: 0; top: 227px; width: 939px; height: 275px; background: var(--band-grey); }
  .steps { left: 68px; top: 229px; }
  .step-label { font-family: "PT Sans Narrow", sans-serif; font-size: 15px; fill: var(--white); }

  .frame { border: 1px dotted var(--frame-dot); background: var(--white); padding: 4px; }
  .hero-frame { top: 289px; height: 193px; }
  .hero-art { width: 100%; height: 100%; }

  .section-title { left: 0; width: 939px; text-align: center; font-family: "PT Sans Narrow", sans-serif; font-size: 19.5px; font-weight: 400; color: var(--ink-dark); }

  .card-frame { width: 172px; padding: 7px; }
  .card-art { width: 100%; height: 143px; }
  .card-name { margin-top: 14px; font-size: 14.5px; font-weight: 700; color: var(--title-blue); }
  .card-maker { margin-top: 6px; font-size: 14.5px; color: var(--muted); }

  .carousel-arrow { width: 18px; height: 48px; }

  .shelf-shadow { left: 70px; width: 800px; height: 12px; background: radial-gradient(ellipse at center top, rgba(0,0,0,0.22), rgba(0,0,0,0) 70%); }

  .footer { left: 0; top: 1119px; width: 939px; height: 81px; background: var(--footer-black); color: var(--white); font-size: 11px; }
  .footer-links { left: 68px; top: 23px; }
  .footer-copy { left: 68px; top: 49px; }
  .social { left: 729px; top: 27px; display: flex; gap: 10px; }
  .social span { width: 28px; height: 28px; display: block; }
  .social .fb { background: #3b5ba8; }
  .social .tw { background: #2a9ad9; }
  .social .rss { background: #f26b1d; }
  .social .yt { background: #d8312b; }
</style>
</head>
<body>
  <div class="abs top-rule"></div>

  <nav class="abs utility-nav">
    <a>HOME</a><a>HOW IT WORKS</a><a>SELL</a><a>CREATE AN ACCOUNT</a><a>CHECK OUT</a><a>LOGIN</a>
  </nav>

  <div class="abs brand"><span class="brand-mark"></span><span class="brand-name">QuillPostly.com</span></div>
  <div class="abs brand-tagline">Hand-Made. Hand-Written. Hand-Delivered</div>

  <div class="abs cart">
    <svg width="16" height="14" viewBox="0 0 16 14" aria-hidden="true"><path d="M1 1h3l2 8h7l2-6H5" fill="none" stroke="#555" stroke-width="1.4"/><circle cx="7" cy="12" r="1.3" fill="#c0392b"/><circle cx="12" cy="12" r="1.3" fill="#c0392b"/></svg>
    Cart (0) items
  </div>

  <div class="abs category-bar">
    <ul class="category-list">
      <li style="left:16px;">UPCOMING HOLIDAYS</li>
      <li style="left:190px;">EVERYDAY CARDS</li>
      <li style="left:339px;">BIRTHDAYS</li>
      <li style="left:447px;">ALL CATEGORIES</li>
    </ul>
    <div class="abs search">Search..
      <svg width="11" height="11" viewBox="0 0 11 11" aria-hidden="true"><circle cx="4.5" cy="4.5" r="3.5" fill="none" stroke="#999" stroke-width="1.5"/><path d="M7 7l3 3" stroke="#999" stroke-width="1.5"/></svg>
    </div>
  </div>

  <div class="abs steps-band"></div>
  <svg class="abs steps" width="805" height="42" viewBox="0 0 805 42">
    <polygon points="528,0 783,0 805,21 783,42 528,42 550,21" fill="var(--step-dark)"/>
    <polygon points="300,0 528,0 550,21 528,42 300,42 322,21" fill="var(--step-mid)"/>
    <polygon points="0,0 301,0 323,21 301,42 0,42" fill="var(--step-blue)"/>
    <text class="step-label" x="50" y="26">STEP 1 : CHOOSE A CARD</text>
    <text class="step-label" x="337" y="27">STEP 2 : CUSTOMIZE IT</text>
    <text class="step-label" x="556" y="27">STEP 3 : WE HANDWRITE AND MAIL</text>
  </svg>

  <div class="abs frame hero-frame" style="left:66px;width:252px;">
    <div class="hero-art" role="img" aria-label="Chalkboard card with a beehive and sweet lettering" style="background:radial-gradient(ellipse at 45% 50%,#5a5a5a 0%,#3a3a3a 45%,#1c1c1c 100%);"></div>
  </div>
  <div class="abs frame hero-frame" style="left:344px;width:252px;">
    <div class="hero-art" role="img" aria-label="Birthday card with a blue paper elephant and stars" style="background:radial-gradient(ellipse at 45% 70%,#7cc3ee 0%,#5aa9e0 38%,#3b3333 72%,#2b2626 100%);"></div>
  </div>
  <div class="abs frame hero-frame" style="left:620px;width:252px;">
    <div class="hero-art" role="img" aria-label="Card with a drawn bluebird on a blossom branch" style="background:radial-gradient(ellipse at 60% 45%,#9cb0c4 0%,#d8d69a 35%,#f6ec9c 70%,#e4dc8e 100%);"></div>
  </div>

  <div class="abs shelf-shadow" style="top:502px;"></div>

  <h2 class="abs section-title" style="top:521px;">UPCOMING HOLIDAYS</h2>

  <svg class="abs carousel-arrow" style="left:76px;top:633px;" viewBox="0 0 18 48" aria-hidden="true"><path d="M15 2L3 24l12 22" fill="none" stroke="#888" stroke-width="1.5"/></svg>
  <svg class="abs carousel-arrow" style="left:846px;top:633px;" viewBox="0 0 18 48" aria-hidden="true"><path d="M3 2l12 22L3 46" fill="none" stroke="#888" stroke-width="1.5"/></svg>

  <div class="abs frame card-frame" style="left:106px;top:560px;height:219px;">
    <div class="card-art" role="img" aria-label="Orange pumpkin photo" style="background:radial-gradient(ellipse at 50% 65%,#f0902a 0%,#d9761c 40%,#8d6a2c 80%,#6f5a2a 100%);"></div>
    <div class="card-name">HALLOWEEN</div><div class="card-maker">BY CREATOR</div>
  </div>
  <div class="abs frame card-frame" style="left:288px;top:560px;height:219px;">
    <div class="card-art" role="img" aria-label="Paper-cut sailboat on pale blue" style="background:linear-gradient(180deg,#cfe3f2 0%,#e6f0f7 40%,#b9d6ec 70%,#2a2a2a 100%);"></div>
    <div class="card-name">COLUMBUS DAY</div><div class="card-maker">BY CREATOR</div>
  </div>
  <div class="abs frame card-frame" style="left:471px;top:560px;height:219px;">
    <div class="card-art" role="img" aria-label="Dog in a helmet before a flag" style="background:linear-gradient(160deg,#b5343d 0%,#e4ddd8 30%,#2f4a8a 55%,#6b655a 80%,#4a4a44 100%);"></div>
    <div class="card-name">VETERAN’S DAY</div><div class="card-maker">BY CREATOR</div>
  </div>
  <div class="abs frame card-frame" style="left:654px;top:560px;height:219px;">
    <div class="card-art" role="img" aria-label="Costumed figure beside a pumpkin" style="background:linear-gradient(120deg,#4f5a3a 0%,#d86f1e 35%,#6b8a4a 55%,#3d4a7a 80%,#2f3462 100%);"></div>
    <div class="card-name">PRESIDENT’S DAY</div><div class="card-maker">BY CREATOR</div>
  </div>

  <h2 class="abs section-title" style="top:797px;">NEW CARDS</h2>

  <svg class="abs carousel-arrow" style="left:76px;top:909px;" viewBox="0 0 18 48" aria-hidden="true"><path d="M15 2L3 24l12 22" fill="none" stroke="#888" stroke-width="1.5"/></svg>
  <svg class="abs carousel-arrow" style="left:846px;top:909px;" viewBox="0 0 18 48" aria-hidden="true"><path d="M3 2l12 22L3 46" fill="none" stroke="#888" stroke-width="1.5"/></svg>

  <div class="abs frame card-frame" style="left:106px;top:836px;height:219px;">
    <div class="card-art" role="img" aria-label="Colourful birthday balloons and creatures" style="background:linear-gradient(180deg,#d6ecf5 0%,#f0a3c8 30%,#f3d25a 55%,#8fc35a 80%,#e46a4a 100%);"></div>
    <div class="card-name">BIRTHDAY</div><div class="card-maker">BY CREATOR</div>
  </div>
  <div class="abs frame card-frame" style="left:288px;top:836px;height:219px;">
    <div class="card-art" role="img" aria-label="Couple beneath a ferris wheel" style="background:radial-gradient(ellipse at 35% 45%,#f7f3ee 0%,#e6ddd2 45%,#c9bdae 100%);"></div>
    <div class="card-name">ANNIVERSARY</div><div class="card-maker">BY CREATOR</div>
  </div>
  <div class="abs frame card-frame" style="left:471px;top:836px;height:219px;">
    <div class="card-art" role="img" aria-label="Floral sympathy card on red" style="background:linear-gradient(180deg,#a32b2b 0%,#eee2c6 12%,#eee2c6 75%,#5a3224 85%,#a32b2b 100%);"></div>
    <div class="card-name">BEREAVEMENT</div><div class="card-maker">BY CREATOR</div>
  </div>
  <div class="abs frame card-frame" style="left:654px;top:836px;height:219px;">
    <div class="card-art" role="img" aria-label="New baby card with pram" style="background:linear-gradient(180deg,#7fcfd4 0%,#f7f3ea 35%,#9fd8e0 60%,#f6d36a 85%,#ef9aa0 100%);"></div>
    <div class="card-name">NEW BABY</div><div class="card-maker">BY CREATOR</div>
  </div>

  <div class="abs shelf-shadow" style="top:1094px;"></div>

  <footer class="abs footer">
    <div class="abs footer-links">About us | FAQ | Contact us</div>
    <div class="abs footer-copy">Copyrights 2013. All Rights Reserved.</div>
    <div class="abs social">
      <span class="fb" role="img" aria-label="Social page"></span>
      <span class="tw" role="img" aria-label="Social page"></span>
      <span class="rss" role="img" aria-label="News feed"></span>
      <span class="yt" role="img" aria-label="Video channel"></span>
    </div>
  </footer>
</body>
</html>
```